Corporate WordPress Site for Global IT Staffing Firm

We are looking for a corporate web presence for our company, Quillex, that is an IT Staffing and Recruiting firm based in Silicon Valley. We want the site to convey strength, confidence and trust in our F500 global customers and be appealing to prospective job seekers looking for their next employment.
I've attached the logo scheme to you. I can provide content within the next few days as well as links to our Chirply, PB pages. I also have wallpaper images selected from Marrow stills for a scrolling banner. Eventually we'll post job openings with search capabilities from a third party VMS SaaS company called Tidewick.
Target Market(s)
Global 1000 companies who purchase staffing from our firm AND prospective job seekers looking for work.
Industry/Entity Type
It Company
Number of Pages Required
3 page
Requirements
Must have
- Modern, parallax design for corporate image. May need links and integration to third party systems in a few months.
- Want each of the images via slider or images to convey:
- Attention to Detail
- Taking the Time to Find the Right Candidates
- Old Fashioned Hard Work
- Assembling the Right Teams
- Built to Scale
Nice to have
- Sliders. Counters. Links to social media pages. Background information. Bio pages. Reference customers.
- Examples of sites we like.
- https://www.rydexo.example/
- http://www.palvinmediaset.example/
- http://www.qornaworks.example/

```html
<!DOCTYPE html>
<html lang="en">
<head>
<meta charset="utf-8">
<title>Quillex — IT Staffing</title>
<link rel="stylesheet" href="https://fonts.googleapis.com/css2?family=Open+Sans:wght@400;600;700&family=Quicksand:wght@500&display=swap">
<style>
  :root {
    --brand: #4f5d8c;
    --brand-dark: #3c4770;
    --ink: #333333;
    --muted: #555555;
    --rule: #c9c9c9;
    --night: #1b1b1b;
    --night-text: #7a7a7a;
    --footer: #262626;
    --footer-base: #1d1d1d;
    --white: #ffffff;
  }
  * { box-sizing: border-box; margin: 0; padding: 0; }
  html, body { width: 1200px; height: 2236px; overflow: hidden; }
  body { position: relative; background: var(--white); font-family: "Open Sans", Arial, sans-serif; color: var(--ink); }

  .abs { position: absolute; }
  .center { left: 0; width: 1200px; text-align: center; }

  /* Header */
  .site-header { position: absolute; left: 0; top: 0; width: 1200px; height: 112px; border-top: 3px solid var(--brand-dark); background: var(--white); }
  .brand { position: absolute; left: 100px; top: 34px; display: flex; align-items: center; gap: 10px; }
  .brand-dot { width: 36px; height: 36px; border-radius: 50%; background: var(--brand); }
  .brand-name { font-size: 34px; font-weight: 700; color: var(--brand); letter-spacing: -1px; }
  .main-nav a { position: absolute; top: 47px; font-size: 12.5px; color: var(--ink); text-decoration: none; text-transform: uppercase; white-space: nowrap; }
  .main-nav a.active { color: var(--brand); }
  .nav-caret { position: absolute; left: 624px; top: 68px; }

  /* Hero */
  .hero { position: absolute; left: 0; top: 112px; width: 1200px; height: 470px;
    background: radial-gradient(ellipse at 55% 40%, #7d7a75 0%, #4b4a49 40%, #232428 80%),
                linear-gradient(#2c2d31, #1d1e21); }
  .hero-title { top: 205px; font-family: "Quicksand", "Open Sans", sans-serif; font-weight: 500; font-size: 56px; color: var(--white); }
  .hero-dots { position: absolute; top: 424px; left: 570px; display: flex; gap: 10px; }
  .hero-dots span { width: 13px; height: 13px; border-radius: 50%; background: var(--white); }
  .hero-dots span.on { background: var(--brand); }

  /* Section headings */
  .section-title { font-size: 22px; color: var(--brand); text-transform: uppercase; font-weight: 400; }
  .section-lead { font-size: 14px; color: var(--muted); }

  /* Services */
  .service { position: absolute; top: 740px; width: 360px; text-align: center; }
  .service svg { display: block; margin: 0 auto; }
  .service h3 { margin-top: 14px; font-size: 18px; font-weight: 400; color: var(--brand); }
  .service hr { width: 100px; margin: 16px auto 13px; border: 0; border-top: 1px solid var(--rule); }
  .service p { font-size: 12.5px; line-height: 24px; color: var(--ink); width: 230px; margin: 0 auto; }

  /* Projects */
  .projects-bg { position: absolute; left: 0; top: 1099px; }
  .project { position: absolute; top: 1264px; width: 236px; }
  .project-photo { width: 236px; height: 164px; }
  .project h4 { margin-top: 16px; font-size: 15px; font-weight: 400; color: #b9c3e6; }
  .project p { margin-top: 8px; font-size: 12px; line-height: 23px; color: var(--night-text); }

  /* Testimonial */
  .quote { top: 1656px; left: 100px; width: 1000px; text-align: center; font-size: 12px; line-height: 26px; color: var(--muted); }
  .avatar { position: absolute; left: 552px; top: 1726px; width: 96px; height: 96px; border-radius: 50%; background: var(--brand); border: 3px solid #d8d8d8; }
  .client-name { top: 1835px; font-size: 12px; font-weight: 700; color: var(--brand); text-transform: uppercase; }
  .client-role { top: 1855px; font-size: 12px; color: var(--brand); }
  .pager { position: absolute; top: 1888px; left: 571px; display: flex; gap: 2px; }
  .pager span { width: 19px; height: 3px; background: #444; }

  /* Footer */
  .site-footer { position: absolute; left: 0; top: 1925px; width: 1200px; height: 264px; background: var(--footer); color: #9a9a9a; }
  .footer-col { position: absolute; top: 43px; }
  .footer-col h5 { font-size: 13px; font-weight: 700; color: var(--white); text-transform: uppercase; line-height: 22px; }
  .footer-col p { font-family: Arial, sans-serif; font-size: 11px; line-height: 21px; margin-top: 16px; }
  .quick-links { list-style: none; margin-top: 15px; font-family: Arial, sans-serif; font-size: 11px; }
  .quick-links li { line-height: 22px; color: #b5b5b5; }
  .news-input { width: 236px; height: 30px; margin-top: 16px; background: #1e1e1e; border: 1px solid #303030; font-family: Arial, sans-serif; font-size: 10px; color: #777; padding: 8px 14px; }
  .news-btn { width: 108px; height: 30px; margin-top: 10px; background: var(--brand); color: var(--white); font-size: 11px; text-align: center; line-height: 30px; text-transform: uppercase; }
  .follow { list-style: none; margin-top: 15px; font-family: Arial, sans-serif; font-size: 11px; }
  .follow li { display: flex; align-items: center; gap: 14px; height: 22px; margin-bottom: 0; line-height: 22px; }
  .follow li + li { margin-top: 0; }
  .follow i { display: block; width: 22px; height: 22px; }
  .footer-base { position: absolute; left: 0; top: 2189px; width: 1200px; height: 47px; background: var(--footer-base); text-align: center; line-height: 47px; font-family: Arial, sans-serif; font-size: 11px; color: #9a9a9a; }
</style>
</head>
<body>

<header class="site-header">
  <div class="brand"><span class="brand-dot"></span><span class="brand-name">Quillex</span></div>
  <nav class="main-nav">
    <a class="active" style="left:609px">Home</a>
    <a style="left:685px">About us</a>
    <a style="left:785px">Services</a>
    <a style="left:879px">Blog</a>
    <a style="left:952px">News</a>
    <a style="left:1026px">Contact us</a>
  </nav>
  <svg class="nav-caret" width="10" height="8" viewBox="0 0 10 8"><path d="M0 0h10L5 8z" fill="#4f5d8c"/></svg>
</header>

<section class="hero" role="img" aria-label="Photograph of skydivers holding hands in a large ring formation high above the ground">
  <h1 class="abs center hero-title">Attention to Detail</h1>
  <div class="hero-dots"><span></span><span class="on"></span><span></span></div>
</section>

<!-- Services -->
<h2 class="abs center section-title" style="top:605px">Out Services</h2>
<svg class="abs" style="left:556px;top:644px" width="88" height="12" viewBox="0 0 88 12">
  <line x1="0" y1="1" x2="88" y2="1" stroke="#d4d4d4"/><path d="M39 1h10l-5 6z" fill="#d4d4d4"/>
</svg>
<p class="abs center section-lead" style="top:666px">At vero eos et accusamus et iusto odio dignissimos ducimus</p>

<div class="service" style="left:53px">
  <svg width="210" height="210" viewBox="0 0 210 210">
    <path d="M105 8 202 105 105 202 8 105z" fill="none" stroke="#222" stroke-width="1.3"/>
    <path d="M114 8 210 105 114 202" fill="none" stroke="#222" stroke-width="1.3"/>
    <path d="M99 20 184 105 99 190 14 105z" fill="none" stroke="#222" stroke-width="1.3"/>
    <path d="M86 96h10l3 4h17v16H86z M86 104h34l-4 12H86z" fill="none" stroke="#4f5d8c" stroke-width="2.6" stroke-linejoin="round"/>
  </svg>
  <h3>On the other hand, we denounce</h3><hr>
  <p>Sed ut perspiciatis unde omnis iste &nbsp;natus error sit voluptatem..</p>
</div>
<div class="service" style="left:420px">
  <svg width="210" height="210" viewBox="0 0 210 210">
    <path d="M105 8 202 105 105 202 8 105z" fill="none" stroke="#222" stroke-width="1.3"/>
    <path d="M114 8 210 105 114 202" fill="none" stroke="#222" stroke-width="1.3"/>
    <path d="M99 20 184 105 99 190 14 105z" fill="none" stroke="#222" stroke-width="1.3"/>
    <path d="M93 99a13 13 0 1 0 14 0" fill="none" stroke="#4f5d8c" stroke-width="4" stroke-linecap="round"/>
    <line x1="100" y1="93" x2="100" y2="106" stroke="#4f5d8c" stroke-width="4" stroke-linecap="round"/>
  </svg>
  <h3>On the other hand, we denounce</h3><hr>
  <p>Sed ut perspiciatis unde omnis iste &nbsp;natus error sit voluptatem..</p>
</div>
<div class="service" style="left:797px">
  <svg width="210" height="210" viewBox="0 0 210 210">
    <path d="M105 8 202 105 105 202 8 105z" fill="none" stroke="#222" stroke-width="1.3"/>
    <path d="M114 8 210 105 114 202" fill="none" stroke="#222" stroke-width="1.3"/>
    <path d="M99 20 184 105 99 190 14 105z" fill="none" stroke="#222" stroke-width="1.3"/>
    <circle cx="100" cy="99" r="7" fill="#4f5d8c"/>
    <path d="M87 120v-5a8 8 0 0 1 8-8h10a8 8 0 0 1 8 8v5z" fill="#4f5d8c"/>
  </svg>
  <h3>On the other hand, we denounce</h3><hr>
  <p>Sed ut perspiciatis unde omnis iste &nbsp;natus error sit voluptatem..</p>
</div>

<!-- Projects -->
<svg class="projects-bg" width="1200" height="454" viewBox="0 0 1200 454">
  <path d="M0 56 552 0H641L1200 56V454H0z" fill="#1b1b1b"/>
</svg>
<h2 class="abs center section-title" style="top:1141px;color:#fff">Our Project</h2>
<svg class="abs" style="left:556px;top:1180px" width="88" height="12" viewBox="0 0 88 12">
  <line x1="0" y1="6" x2="88" y2="6" stroke="#555"/><path d="M44 2l4 4-4 4-4-4z" fill="#ccc"/>
</svg>
<p class="abs center" style="top:1204px;font-size:12.5px;color:#555">At vero eos et accusamus et iusto odio dignissimos ducimus qui blanditiis praesentium dignissimos ducimus voluptatum...</p>

<div class="project" style="left:100px">
  <div class="project-photo" role="img" aria-label="Photograph of a tape measure and pencil on wood" style="background:linear-gradient(120deg,#e6e2da,#b8a58a 60%,#6b5a45)"></div>
  <h4>Nam libero tempore</h4>
  <p>Sed ut perspiciatis unde omnis iste natus quasi architecto vitae explicabo.</p>
</div>
<div class="project" style="left:356px">
  <div class="project-photo" role="img" aria-label="Photograph of blue network cables in a server patch panel" style="background:linear-gradient(160deg,#3c63d6,#1d3aa8 55%,#0d1a55)"></div>
  <h4>Nam libero tempore</h4>
  <p>Sed ut perspiciatis unde omnis iste natus quasi architecto vitae explicabo.</p>
</div>
<div class="project" style="left:611px">
  <div class="project-photo" role="img" aria-label="Photograph of orange fibre cables plugged into a switch" style="background:linear-gradient(180deg,#cfcac4 0%,#e2661e 30%,#c2260f 70%,#3a0a05)"></div>
  <h4>Nam libero tempore</h4>
  <p>Sed ut perspiciatis unde omnis iste natus quasi architecto vitae explicabo.</p>
</div>
<div class="project" style="left:866px">
  <div class="project-photo" role="img" aria-label="Photograph of a worker carrying a heavy load in a dim workshop" style="background:radial-gradient(ellipse at 50% 50%,#8a5a4a,#3a2722 55%,#141414)"></div>
  <h4>Nam libero tempore</h4>
  <p>Sed ut perspiciatis unde omnis iste natus quasi architecto vitae explicabo.</p>
</div>

<!-- Testimonial -->
<h2 class="abs center section-title" style="top:1578px">Testimonial</h2>
<svg class="abs" style="left:556px;top:1616px" width="88" height="12" viewBox="0 0 88 12">
  <line x1="0" y1="6" x2="88" y2="6" stroke="#999"/><path d="M44 2l4 4-4 4-4-4z" fill="#333"/>
</svg>
<p class="abs quote">At vero eos et accusamus et iusto odio dignissimos ducimus qui blanditiis praesentium voluptatum deleniti atque corrupti quos dolores et quas molestias excepturi sint occaecati cupiditate non provident, similique suntin culpa qui officia deserunt mollitia animi, id est laborum et dolorum fuga.</p>
<div class="avatar"></div>
<p class="abs center client-name">Nam libero tepore</p>
<p class="abs center client-role">Heart patient</p>
<div class="pager"><span></span><span></span><span></span></div>

<!-- Footer -->
<footer class="site-footer">
  <div class="footer-col" style="left:100px;width:310px">
    <h5>On the other hand, we denounce</h5>
    <p>Sed ut perspiciatis unde omnis iste natus error sit voluptatem accusantium doloremque laudantium, totam rem aperiam, eaque ipsa quae ab illo inventore veritatis et quasi architecto beatae vitae dicta sunt explicabo. Nemo enim ipsam voluptatem quia voluptas sit magni dolores eos qui ratione voluptatem sequi nesciunt.</p>
  </div>
  <div class="footer-col" style="left:468px">
    <h5>Quick links</h5>
    <ul class="quick-links"><li>Home</li><li>About us</li><li>News</li><li>Blog</li><li>Projects</li><li>Contact us</li></ul>
  </div>
  <div class="footer-col" style="left:640px;width:240px">
    <h5>Subscribe<br>Newsletter signup</h5>
    <p style="margin-top:10px;color:#8f9bc6">At vero eos et accusamus et iusto odio dignissimos ducimus</p>
    <div class="news-input">Newsletter signup</div>
    <div class="news-btn">Subscribe</div>
  </div>
  <div class="footer-col" style="left:957px">
    <h5>Follow us</h5>
    <ul class="follow">
      <li><i style="background:#3b5a98"></i>Pagebook</li>
      <li style="margin-top:9px"><i style="background:#2aa9e0"></i>Chirply</li>
      <li style="margin-top:9px"><i style="background:#d6382b"></i>Globe Plus</li>
      <li style="margin-top:9px"><i style="background:#ef7a22"></i>Rss</li>
    </ul>
  </div>
</footer>
<div class="footer-base">© 2015 - &nbsp;Quillex - All rights reserved</div>

</body>
</html>
```